Mx K's - CD Cover Project number 7

Hi All,

I manage a small sound recording studio and need assistance with CD artwork, notably converting pdf image files to Photoshop, on print-ready templates, to submit to my CD duplication and packaging service

CD Name: “Where'd It Go?”, artist's name: “Mx. K’s Fine Tonic”.

In addition to the technical skill required to convert my images to Photoshop format, some creative design flair is desirable: the attractive superimposition of text (e.g., CD title and artist, liner notes, song titles, etc.) onto images, and the creation of professional-looking CD labels, is also required.

So I need a cover created using the images provided with the title and details superimposed.

I have planned on a folded rectangular insert to give 4 squarish pages – printed in color on one side of the rectangle, and monochromatic on the other.

I have executed this as a mock up, which you can view in 3 scans. Scan [ "… 0018.jpeg" ] is the cover, or page 1, which will be visible through the jewel case
and the RIGHT-HAND half of a rectangle to be folded in two.

Scan [“…0019.jpeg” ] is the LEFT-HAND half of the same rectangle – though it should be rendered in COLOR, not B&W. Once the rectangle is folded, it becomes the 4th page, or back, of the insert. and

To recapitulate: the color side of the virtual rectangle, once the pictures in [ “…0019.jpeg” ] are properly rendered in color, would constitute the front "cover" [“...0018.jpeg” ] – visible through the plastic jewel case – plus the back of the insert
[ “…0019.jpeg “].

Scan “.0026.jpeg” is the mockup of the inside of the folded rectangle (pages 3 & 4) and constitutes the liner notes. The liner notes are provided as ".doc" file [ "WHERE'D IT GO? liner notes & song list.docx" ].

I would like to see the old-fashioned picture on the bottom right of the liner notes scan expanded, and used as a lightly-rendered background photo on which the liner notes text is superimposed across the entire rectangle (pages 3 & 4), rather than used as a little picture at the end (as it is in the mockup).

Attached to the brief are all the actual photos used for the mockups. This particular picture [ "Scan...20031.jpg" ] is degraded in the project folder "Where'd It Go?". A cleaner version will be attached to the brief separately. It is file [ "...10000.jpeg"] (Alternatively, the image could be lifted from the scan, although it has been cropped a bit.)

Again, these scans are only of the mockup.

The name of the band [Mx. K’s Fine Tonic] , and the name of the CD [Where'd It Go?], would need to be added to page 1 (front cover, or RIGHT-HAND SIDE of rectangle before folding), or Scan [“…0018.jpeg”], in some funky old (1920’s or 1930’s-style) font – without obscuring the faces of the band.

The text of the liner notes and the song list are contained in the ".doc" file "WHERE'D IT GO? liner notes & song list.docx".

The name of the band and the song list needs to be added to the back tray card, which is mocked up as scan [ “.0027.jpeg” ].

The "Pallid Comet Records" logo [see ".psd" file] also needs to go on the back tray card.

The name of the band and the name of the CD need also to go on the spine (edge).

A monochromatic CD label would have to be designed. I would like to see a suitable background picture (perhaps a 1920’s train image or cityscape, or a picture of the band) with the band name and CD title, and song list. (The folder contains a mockup of a CD label, which I constructed from clip art.)

If more pix are requested/desirable, I would be happy to provide additional ones. Scan [ "...10000.jpeg" ] is a sample from an earlier cassette version of this CD.

Guidelines for setup are provided by the duplication company, "Dorvex". These are available at:
http://dorvex.platepresshub.example/Quoter/Templates.aspx

Target Market(s)

All ages, all socioeconomic groups, who like to have a good time.

Industry/Entity Type

Recording Studio

Requirements
Must have
• A funky, old-fashioned feel. The music is all from the 1920's and 1930's - honky tonk, blues, and "jug band" style. Therefore fonts, and artistic treatments should be reflective of those times, not modern, new age, psychedelic, or anything suggestive of "rock & roll".
Nice to have
• A lightly-rendered picture as a background picture for superimposed liner notes.
Should not have
• Anything flashy, psychedelic, hyper-abstract.

```html
<!DOCTYPE html>
<html lang="en">
<head>
<meta charset="utf-8">
<title>Mx. K’s Fine Tonic – Where'd It Go? – Back Tray Card</title>
<link rel="stylesheet" href="https://fonts.googleapis.com/css2?family=Playfair+Display+SC:wght@700;900&family=Libre+Baskerville:wght@700&display=swap">
<style>
  :root {
    --paper: #ffffff;
    --cream: #fcf3bf;
    --navy: #1c2378;
    --track-fill: #9cc2f2;
    --track-edge: #14204f;
    --crop: #9a9a9a;
    --logo-ink: #2a2a2a;
  }
  html, body { margin: 0; padding: 0; overflow: hidden; background: var(--paper); }
  .canvas { position: relative; width: 1200px; height: 1050px; overflow: hidden; background: var(--paper); }
  .crop-marks { position: absolute; inset: 0; }
  .tray-card { position: absolute; left: 70px; top: 110px; width: 1075px; height: 855px; background: var(--cream); }
  .photo { position: absolute; }
  .photo-hat { left: 175px; top: 163px; width: 170px; height: 233px; background: linear-gradient(160deg, #7a6a5a, #3b332d 60%, #8a7c6c); }
  .photo-band-sepia { left: 345px; top: 152px; width: 698px; height: 523px; background: radial-gradient(ellipse at 60% 45%, #cbb27a, #a8925e 55%, #7d6a43); }
  .photo-porch { left: 175px; top: 405px; width: 170px; height: 200px; background: linear-gradient(180deg, #8d8576, #5e5446 55%, #a39a88); }
  .photo-washboard { left: 175px; top: 610px; width: 240px; height: 285px; background: linear-gradient(170deg, #5c4a56, #3a2c33 50%, #7b6a5c); }
  .photo-street { left: 420px; top: 665px; width: 205px; height: 230px; background: linear-gradient(180deg, #8e96a0, #5d5a57 60%, #6d6456); }
  .photo-storefront { left: 665px; top: 665px; width: 220px; height: 230px; background: linear-gradient(180deg, #9aa3ad, #6b6660 55%, #574c40); }
  .spine { position: absolute; top: 110px; height: 855px; width: 105px; }
  .spine-left { left: 70px; }
  .spine-right { left: 1043px; }
  .spine-text {
    position: absolute; left: 50%; white-space: nowrap;
    font-family: "Playfair Display SC", serif; font-weight: 900; color: var(--navy);
    font-size: 26px; letter-spacing: 1px;
  }
  .spine-left .spine-text { transform: translate(-50%, -50%) rotate(-90deg); }
  .spine-right .spine-text { transform: translate(-50%, -50%) rotate(90deg); }
  .spine-left .album { top: 195px; font-size: 22px; }
  .spine-left .band { top: 580px; }
  .spine-right .band { top: 265px; }
  .spine-right .album { top: 600px; font-size: 22px; }
  .band-title {
    position: absolute; left: 421px; top: 150px; margin: 0; line-height: 1;
    font-family: "Playfair Display SC", serif; font-weight: 900; font-size: 50px;
    color: var(--navy); text-shadow: 2px 2px 0 rgba(255,255,255,0.55); letter-spacing: 3px; white-space: nowrap;
  }
  .track-list {
    position: absolute; left: 280px; top: 258px; width: 660px; margin: 0; padding: 0; list-style: none; text-align: center;
    font-family: "Libre Baskerville", serif; font-weight: 700; font-size: 20px; line-height: 31.5px;
    color: var(--track-fill); letter-spacing: 3px; white-space: nowrap;
    text-shadow: -1.5px -1.5px 0 var(--track-edge), 1.5px -1.5px 0 var(--track-edge), -1.5px 1.5px 0 var(--track-edge), 1.5px 1.5px 0 var(--track-edge);
  }
  .track-list .num { margin-right: 12px; }
  .label-mark { position: absolute; left: 925px; top: 800px; width: 105px; height: 75px; background: #f4efe2; display: flex; flex-direction: column; align-items: center; justify-content: center; gap: 4px; }
  .label-mark .dot { width: 14px; height: 14px; border-radius: 50%; background: var(--logo-ink); }
  .label-mark .name { font-family: "Libre Baskerville", serif; font-weight: 700; font-size: 9px; color: var(--logo-ink); text-align: center; line-height: 11px; }
  .label-url { position: absolute; left: 918px; top: 882px; width: 120px; text-align: center; font-family: "Libre Baskerville", serif; font-weight: 700; font-size: 8px; color: var(--logo-ink); letter-spacing: 0.5px; }
</style>
</head>
<body>
<div class="canvas">
  <svg class="crop-marks" width="1200" height="1050" aria-hidden="true">
    <g stroke="var(--crop)" stroke-width="1">
      <line x1="70" y1="0" x2="70" y2="95"/><line x1="175" y1="0" x2="175" y2="95"/>
      <line x1="1043" y1="0" x2="1043" y2="95"/><line x1="1145" y1="0" x2="1145" y2="95"/>
      <line x1="0" y1="110" x2="55" y2="110"/><line x1="1160" y1="110" x2="1200" y2="110"/>
      <line x1="70" y1="980" x2="70" y2="1050"/><line x1="175" y1="980" x2="175" y2="1050"/>
      <line x1="1043" y1="980" x2="1043" y2="1050"/><line x1="1145" y1="980" x2="1145" y2="1050"/>
      <line x1="0" y1="965" x2="55" y2="965"/><line x1="1160" y1="965" x2="1200" y2="965"/>
    </g>
  </svg>

  <div class="tray-card"></div>

  <div class="photo photo-band-sepia" role="img" aria-label="Sepia photo of the band at a table"></div>
  <div class="photo photo-hat" role="img" aria-label="Photo of a musician in a hat"></div>
  <div class="photo photo-porch" role="img" aria-label="Photo of band members outdoors"></div>
  <div class="photo photo-washboard" role="img" aria-label="Photo of a musician playing washboard"></div>
  <div class="photo photo-street" role="img" aria-label="Photo of the band on a street"></div>
  <div class="photo photo-storefront" role="img" aria-label="Photo of band members by a storefront"></div>

  <div class="spine spine-left">
    <span class="spine-text album">Where'd It Go?</span>
    <span class="spine-text band">Mx. K’s Fine Tonic</span>
  </div>
  <div class="spine spine-right">
    <span class="spine-text band">Mx. K’s Fine Tonic</span>
    <span class="spine-text album">Where'd It Go?</span>
  </div>

  <h1 class="band-title">Mx. K’s Fine Tonic</h1>

  <ol class="track-list">
    <li><span class="num">1.</span>Spend Your Dime</li>
    <li><span class="num">2.</span>That's No Way to Treat a Pal</li>
    <li><span class="num">3.</span>Mr. Biscuit Maker</li>
    <li><span class="num">4.</span>Where'd It Go?</li>
    <li><span class="num">5.</span>Chapel Door Blues</li>
    <li><span class="num">6.</span>Walk It Soft And Low</li>
    <li><span class="num">7.</span>I Won't Be Troubled</li>
    <li><span class="num">8.</span>River Bottom High Water Blues</li>
    <li><span class="num">9.</span>That Won't Come Round No More</li>
    <li><span class="num">10.</span>Lone Boy Miles Away from Home</li>
    <li><span class="num">11.</span>Cornet Player's Blues</li>
    <li><span class="num">12.</span>Lamplight</li>
    <li><span class="num">13.</span>Evening Rag</li>
    <li><span class="num">14.</span>Roll On Down the Track</li>
  </ol>

  <div class="label-mark">
    <span class="dot"></span>
    <span class="name">Pallid Comet<br>Records</span>
  </div>
  <div class="label-url">www.pallidcomet.com</div>
</div>
</body>
</html>
```